3 Flyer Project: Industrial, Civil, and Commercial

Total of 3 separate flyers that go together to be put in folders for marketing. The three flyer categories will be Industrial, Civil, and Commercial. I will upload three photos for each flyer and verbiage for each flyer. The photos may change upon final revisions. We want creativity and not just bullet points on a page.

FLYER #1 INDUSTRIAL

INDUSTRIAL EXPERIENCE:
BRELLANT COMPANY
VESKAR
OAKMOOR PIT MINE
GALDWYN FORGE STEEL
PERNOTH QUARTZWORKS
DUNMARROW VALE LOOP RAILWAY

INDUSTRIAL FOCUS AREAS:
PLANT FACILITY WATER SYSTEMS
HEAVY CONCRETE
FACILITY REPAIR
INDUSTRIAL UPGRADES
RAILWAYS AND MANUFACTURING

INDUSTRIAL SOLUTIONS:
WE MAINTAIN AN EXTENSIVE LEVEL OF DETAIL AND INNOVATIVE PROBLEM-SOLVING TALENTS TO DELIVER HIGH QUALITY, SUSTAINABLE SOLUTIONS.

FLYER #2 CIVIL

CIVIL EXPERIENCE:
VELDORAN DEPT. OF TRANSPORTATION
KESTRIA DEPT. OF TRANSPORTATION
PLOVENDA DEPT. OF TRANSPORTATION
BUREAU OF WORKSMITHS
NATIONAL SKYWAYS AUTHORITY BOARD
MINISTRY OF GUARDIANSHIP

CIVIL FOCUS AREAS:
AIRFIELD
STREETSCAPES
STORM DRAINAGE
UTILITY UPGRADES
BOX CULVERTS
RETAINING WALLS

CIVIL SOLUTIONS:
WE SPECIALIZE IN COMPLEX CIVIL PROJECTS.

FLYER #3 COMMERCIAL

COMMERCIAL EXPERIENCE:
HOLLENBRAKE UPLANDS UNIVERSITY
VELDORAN OFFICE OF STRUCTURES
TOWN OF BRANWICK, MISSISSIPPI
TOWN OF MERRODA, MISSISSIPPI
ACADEMY FOR ADVANCED STUDIES

COMMERCIAL FOCUS AREAS:
NEW CONSTRUCTION
RENOVATIONS
STRUCTURAL FOUNDATIONS
STRUCTURAL UPGRADES

COMMERCIAL SOLUTIONS:
WE NOT ONLY KNOW HOW ALL THE PARTS AND PIECES FIT TOGETHER WITHIN A PROJECT, BUT WE SPECIALIZE IN THE SELF PERFORMANCE OF MANY DIVISIONS WHICH DIFFERENTIATES US FROM MANY OTHER GENERAL CONTRACTORS.

Marketing

• 3 photos on each flyer based on the Industrial, Commercial, and Civil flyers description. Our company logo as well as descriptions shown for each flyer. The blue we use in our logo cmyk is 100-80-0-22

```html
<!DOCTYPE html>
<html lang="en">
<head>
<meta charset="utf-8">
<title>Harlowe Construction – Industrial Flyer</title>
<link rel="stylesheet" href="https://fonts.googleapis.com/css2?family=Comfortaa:wght@500&family=Montserrat:wght@500;600;700&family=Oswald:wght@600&family=Source+Sans+3:wght@400;600&family=Lato:wght@400;700&display=swap">
<style>
:root{
  --brand-blue:#1f3c98;
  --brand-blue-dark:#182f7a;
  --ink:#222;
  --body-grey:#555;
  --tab-grey:#6b6b6b;
  --footer-light:#e6e6e6;
  --footer-dark:#4d4d4d;
  --page-bg:#d8d5d1;
  --white:#fff;
}
*{margin:0;padding:0;box-sizing:border-box}
html,body{width:1200px;height:1200px;overflow:hidden;background:var(--page-bg)}
.flyer{position:absolute;left:151px;top:20px;width:932px;height:1205px;background:var(--white);
  transform:scale(.963);transform-origin:0 0;box-shadow:0 6px 18px rgba(0,0,0,.25);overflow:hidden}
.hero{position:absolute;left:0;top:0}
.brand{position:absolute;left:62px;top:62px;display:flex;align-items:center;gap:12px}
.brand-square{width:60px;height:60px;background:var(--brand-blue)}
.brand-name{font-family:"Oswald",sans-serif;font-weight:600;color:var(--brand-blue);font-size:30px;line-height:32px;letter-spacing:1px}
.values{position:absolute;top:0;left:0;width:932px}
.value-badge{position:absolute;top:486px;width:76px;height:76px}
.value-label{position:absolute;top:577px;width:300px;text-align:center;font-family:"Comfortaa",sans-serif;font-weight:500;font-size:23px;color:var(--ink)}
.section-title{position:absolute;top:642px;left:0;width:932px;text-align:center;font-family:"Montserrat",sans-serif;font-weight:600;font-size:20px;color:var(--brand-blue)}
.clients{position:absolute;top:684px;left:54px;display:flex;gap:6px}
.client{width:132px;height:59px;border:1px solid #cfcfcf;display:flex;align-items:center;justify-content:center;text-align:center;
  font-family:"Montserrat",sans-serif;font-weight:700;font-size:11px;line-height:13px;color:var(--brand-blue);padding:0 6px}
.focus{position:absolute;left:0;top:799px;width:932px;height:233px;background:var(--brand-blue)}
.focus-tab{position:absolute;left:294px;top:-15px;width:344px;height:38px;background:var(--tab-grey);border-radius:8px 8px 10px 10px;
  color:var(--white);font-family:"Montserrat",sans-serif;font-weight:500;font-size:20px;letter-spacing:.5px;display:flex;align-items:center;justify-content:center}
.focus-item{position:absolute;display:flex;align-items:center;gap:12px;font-family:"Source Sans 3",sans-serif;font-size:19px;color:var(--white)}
.focus-item svg{width:50px;height:54px}
.solutions{position:absolute;left:53px;top:1049px;width:830px}
.solutions h2{font-family:"Montserrat",sans-serif;font-weight:600;font-size:20px;color:var(--brand-blue)}
.solutions p{margin-top:10px;font-family:"Lato",sans-serif;font-size:14.5px;color:var(--body-grey)}
.footer{position:absolute;left:0;top:1132px;width:932px;height:73px}
.footer-bar{position:absolute;left:0;top:0;width:932px;height:50px;background:var(--footer-light)}
.footer-base{position:absolute;left:0;top:50px;width:932px;height:23px;background:var(--footer-dark)}
.footer-info{position:absolute;top:15px;display:flex;align-items:center;gap:8px;font-family:"Lato",sans-serif;font-size:13.5px;color:#444}
.footer-phone{position:absolute;left:718px;top:10px;display:flex;align-items:center;gap:12px;font-family:"Lato",sans-serif;font-weight:700;font-size:21px;color:var(--white)}
</style>
</head>
<body>
<main class="flyer">
  <svg class="hero" width="932" height="524" viewBox="0 0 932 524">
    <defs>
      <linearGradient id="plantScene" x1="0" y1="0" x2="0" y2="1">
        <stop offset="0" stop-color="#ffffff"/>
        <stop offset=".4" stop-color="#dfe8f2"/>
        <stop offset=".62" stop-color="#b9bdb8"/>
        <stop offset=".75" stop-color="#6f8d4a"/>
        <stop offset="1" stop-color="#4f7a2c"/>
      </linearGradient>
      <linearGradient id="nightPour" x1="0" y1="0" x2="0" y2="1">
        <stop offset="0" stop-color="#1d2233"/>
        <stop offset=".6" stop-color="#3a3a3a"/>
        <stop offset="1" stop-color="#7a5634"/>
      </linearGradient>
      <linearGradient id="formwork" x1="0" y1="0" x2="0" y2="1">
        <stop offset="0" stop-color="#6f8f55"/>
        <stop offset=".25" stop-color="#c3a27a"/>
        <stop offset="1" stop-color="#b5784a"/>
      </linearGradient>
    </defs>
    <polygon points="0,0 468,0 600,260 478,522 0,522" fill="url(#plantScene)" role="img" aria-label="Photo: power plant with cooling towers behind green field"/>
    <polygon points="484,0 932,0 932,259 611,259" fill="url(#nightPour)" role="img" aria-label="Photo: night concrete pour with pump truck at plant"/>
    <polygon points="611,265 932,265 932,522 490,522" fill="url(#formwork)" role="img" aria-label="Photo: timber formwork for foundation on site"/>
    <polyline points="470,0 602,260 482,522" fill="none" stroke="var(--brand-blue)" stroke-width="6"/>
    <rect x="0" y="520" width="932" height="4" fill="var(--brand-blue)"/>
  </svg>

  <div class="brand">
    <div class="brand-square"></div>
    <div class="brand-name">HARLOWE<br>CONSTRUCTION</div>
  </div>

  <section class="values">
    <svg class="value-badge" style="left:115px" viewBox="0 0 76 76">
      <circle cx="38" cy="38" r="37" fill="var(--brand-blue)"/><circle cx="38" cy="38" r="31" fill="none" stroke="#fff" stroke-width="2"/>
      <circle cx="38" cy="38" r="12" fill="none" stroke="#fff" stroke-width="5" stroke-dasharray="4 3"/><circle cx="38" cy="38" r="6" fill="#fff"/>
    </svg>
    <svg class="value-badge" style="left:435px" viewBox="0 0 76 76">
      <circle cx="38" cy="38" r="37" fill="var(--brand-blue)"/><circle cx="38" cy="38" r="31" fill="none" stroke="#fff" stroke-width="2"/>
      <path d="M25 51 L51 25 M25 25 L51 51" stroke="#fff" stroke-width="6" stroke-linecap="round"/>
    </svg>
    <svg class="value-badge" style="left:745px" viewBox="0 0 76 76">
      <circle cx="38" cy="38" r="37" fill="var(--brand-blue)"/><circle cx="38" cy="38" r="31" fill="none" stroke="#fff" stroke-width="2"/>
      <rect x="20" y="27" width="24" height="18" fill="#fff"/><path d="M44 32 H52 L57 39 V45 H44Z" fill="#fff"/>
      <circle cx="28" cy="48" r="4" fill="#fff" stroke="var(--brand-blue)" stroke-width="2"/><circle cx="50" cy="48" r="4" fill="#fff" stroke="var(--brand-blue)" stroke-width="2"/>
    </svg>
    <div class="value-label" style="left:22px">Quality Construction</div>
    <div class="value-label" style="left:330px">Innovative Solutions</div>
    <div class="value-label" style="left:623px">First class Delivery</div>
  </section>

  <h2 class="section-title">INDUSTRIAL EXPERIENCE :</h2>
  <ul class="clients" style="list-style:none">
    <li class="client">BRELLANT COMPANY</li>
    <li class="client">VESKAR</li>
    <li class="client">OAKMOOR PIT MINE</li>
    <li class="client">GALDWYN FORGE STEEL</li>
    <li class="client">PERNOTH QUARTZWORKS</li>
    <li class="client">DUNMARROW VALE LOOP RAILWAY</li>
  </ul>

  <section class="focus">
    <div class="focus-tab">INDUSTRIAL FOCUS AREAS</div>
    <div class="focus-item" style="left:53px;top:55px">
      <svg viewBox="0 0 50 54"><polygon points="25,2 47,14 47,40 25,52 3,40 3,14" fill="none" stroke="#fff" stroke-width="1.5"/><rect x="13" y="21" width="16" height="12" fill="#fff"/><path d="M29 25h6l4 5v3H29z" fill="#fff"/><circle cx="18" cy="35" r="3" fill="#fff"/><circle cx="34" cy="35" r="3" fill="#fff"/></svg>
      <span>Heavy concrete</span>
    </div>
    <div class="focus-item" style="left:378px;top:55px">
      <svg viewBox="0 0 50 54"><polygon points="25,2 47,14 47,40 25,52 3,40 3,14" fill="none" stroke="#fff" stroke-width="1.5"/><path d="M12 36V26l7 4v-4l7 4v-4l7 4V17h4v19z" fill="#fff"/></svg>
      <span>Industrial upgrades</span>
    </div>
    <div class="focus-item" style="left:699px;top:55px">
      <svg viewBox="0 0 50 54"><polygon points="25,2 47,14 47,40 25,52 3,40 3,14" fill="none" stroke="#fff" stroke-width="1.5"/><path d="M19 16v22M31 16v22" stroke="#fff" stroke-width="4" stroke-linecap="round"/></svg>
      <span>Facility repair</span>
    </div>
    <div class="focus-item" style="left:53px;top:138px">
      <svg viewBox="0 0 50 54"><polygon points="25,2 47,14 47,40 25,52 3,40 3,14" fill="none" stroke="#fff" stroke-width="1.5"/><path d="M14 20h18v5h-6v4h-4v-4h-8z" fill="#fff"/><path d="M13 36q4-3 8 0t8 0t8 0" stroke="#fff" stroke-width="2" fill="none"/></svg>
      <span>Plant facility water systems</span>
    </div>
    <div class="focus-item" style="left:378px;top:138px">
      <svg viewBox="0 0 50 54"><polygon points="25,2 47,14 47,40 25,52 3,40 3,14" fill="none" stroke="#fff" stroke-width="1.5"/><rect x="16" y="15" width="18" height="20" rx="4" fill="none" stroke="#fff" stroke-width="2.5"/><path d="M16 26h18M18 40l-3 3M32 40l3 3" stroke="#fff" stroke-width="2.5"/></svg>
      <span>Railways and manufacturing</span>
    </div>
  </section>

  <section class="solutions">
    <h2>Industrial Solutions :</h2>
    <p>We maintain an extensive level of detail and innovative problem-solving talents to deliver high quality, sustainable solutions.</p>
  </section>

  <footer class="footer">
    <div class="footer-bar"></div>
    <div class="footer-base"></div>
    <svg style="position:absolute;left:0;top:0" width="932" height="73" viewBox="0 0 932 73">
      <polygon points="712,0 932,0 932,50 672,50" fill="var(--footer-dark)"/>
      <polygon points="700,0 710,0 670,50 660,50" fill="var(--brand-blue)"/>
    </svg>
    <div class="footer-info" style="left:53px">
      <svg width="20" height="18" viewBox="0 0 20 18"><path d="M10 1L1 9h3v8h4v-5h4v5h4V9h3z" fill="var(--brand-blue)"/></svg>
      <span>2290 Foundry Row Ashcombe, Veldora 40612</span>
    </div>
    <div class="footer-info" style="left:450px">
      <svg width="18" height="18" viewBox="0 0 18 18"><circle cx="9" cy="9" r="7.5" fill="none" stroke="var(--brand-blue)" stroke-width="1.6"/><path d="M1.5 9h15M9 1.5c-4 4-4 11 0 15M9 1.5c4 4 4 11 0 15" fill="none" stroke="var(--brand-blue)" stroke-width="1.3"/></svg>
      <span>www.harloweconstruction.com</span>
    </div>
    <div class="footer-phone">
      <svg width="20" height="20" viewBox="0 0 20 20"><path d="M5 2l3 4-2 2c1 3 3 5 6 6l2-2 4 3-2 3C9 18 2 11 2 4z" fill="none" stroke="#fff" stroke-width="1.6"/></svg>
      <span>555.214.0386</span>
    </div>
  </footer>
</main>
</body>
</html>
```